Health Benefits Association Website Design

The Unified Household Wellspring Alliance (UHWA) is an organization formed for the purpose of providing its members better value for selected health benefits and services. Members can use the association benefits either in conjunction with or independently of other medical insurance they may have. Some of the benefits available include discounted dental and vision care and prescription mail order services. There is no limitation on who can join. This membership will be primarily marketed as a way to enhance the value of a fixed benefit health insurance plan although members do not have to have the insurance plan join the association.

We are seeking a design for a website to be used for consumers to get information about membership and for current members to be able to access their benefits. The website should include:

1) A landing page to provide a description of the UHWA

2) A secondary page that can be duplicated that will:
a. Provide a list of benefits
b. Provide a membership enrollment form
c. Provide a member’s only access page
d. Provide a contact page for more information

We are seeking a modern but conservative design that will reflect value, simplicity and good health. The site design will also need to be compatible for use with mobile phones and tablets.

A copy of the association logo is included with the submission. It will also need to be incorporated into the website design. Layouts of similar association websites have also been included for reference.

Target Market(s)

Ages 25 to 65 unmarried, married with no children, professionals, self-employed, active and healthy

Industry/Entity Type

Health And Wellness

Number of Pages Required

2 page

Font styles to use
Sans Serif

Colors

Designer to choose colors to be used in the design.

Requirements
Must have
• UHWA Logo (attached). Use colors from the logo in the website design.
Nice to have
• Graphics, if used, should convey health and fitness and skew toward a diverse array of adults 25 to 40.

```html
<!DOCTYPE html>
<html lang="en">
<head>
<meta charset="utf-8">
<title>Unified Household Wellspring Alliance</title>
<link href="https://fonts.googleapis.com/css2?family=Roboto:wght@400;500;700&family=Roboto+Condensed:wght@400;700&display=swap" rel="stylesheet">
<style>
:root{
  --olive:#8a9a3e;
  --olive-dark:#77872f;
  --yellow:#f2c315;
  --yellow-deep:#e8b70c;
  --ink:#1e1e1e;
  --dark:#262626;
  --text:#333;
  --muted:#555;
  --white:#fff;
}
*{box-sizing:border-box;margin:0;padding:0}
html,body{width:1200px;height:2835px;overflow:hidden;background:var(--white)}
body{font-family:"Roboto",Arial,sans-serif;color:var(--text)}
.page{position:relative;width:1200px;height:2835px;overflow:hidden}
.abs{position:absolute}
.btn{position:absolute;display:flex;align-items:center;justify-content:center;gap:8px;font-family:"Roboto Condensed",Arial,sans-serif;font-weight:700;text-transform:uppercase;letter-spacing:.3px}
.btn svg{width:15px;height:15px}

/* header */
.topbar{top:0;left:0;width:1200px;height:76px;background:var(--dark)}
.hero{top:76px;left:0;width:1200px;height:533px;background:linear-gradient(100deg,#f3f1ee 0%,#e9e4dc 35%,#d8cbbb 60%,#cdbfae 80%,#e4ddd3 100%)}
.hero-tag{top:430px;left:161px;font-family:"Roboto Condensed",Arial,sans-serif;font-weight:700;font-size:22px;line-height:24px;color:#9a9a9a;text-transform:uppercase}
.brand{top:-5px;left:510px;width:180px;height:175px;border-radius:0 0 90px 90px;background:var(--dark);display:flex;align-items:center;justify-content:center;text-align:center;padding:40px 22px 20px}
.brand-name{font-family:"Roboto Condensed",Arial,sans-serif;font-weight:700;font-size:16px;line-height:19px;color:var(--yellow);text-transform:uppercase}

.promo{top:609px;left:0;width:1200px;height:81px;background:var(--olive)}
.promo-text{top:639px;left:161px;font-family:"Roboto Condensed",Arial,sans-serif;font-weight:700;font-size:20px;color:var(--white);text-transform:uppercase}
.join{top:632px;left:902px;width:136px;height:37px;background:var(--yellow);color:var(--ink);font-size:17px}

/* welcome */
.welcome-frame{top:752px;left:161px;width:285px;height:353px;background:#8f8f8f}
.welcome-photo{top:741px;left:174px;width:285px;height:352px;background:linear-gradient(160deg,#c9b79c,#e6dccb 45%,#9aa36b 80%,#6f7a45);border:3px solid var(--white)}
.welcome-title{top:728px;left:497px;font-family:"Roboto Condensed",Arial,sans-serif;font-weight:700;font-size:38px;color:var(--olive)}
.welcome-sub{top:772px;left:497px;font-size:23px;font-weight:400;color:var(--ink)}
.welcome-body{top:812px;left:497px;width:545px;font-size:10px;line-height:18.3px;color:var(--muted)}
.welcome-body p+p{margin-top:12px}
.read-more{top:1072px;left:499px;width:132px;height:37px;background:var(--olive);color:var(--white);font-size:14px}

/* benefits */
.section-title{font-family:"Roboto Condensed",Arial,sans-serif;font-weight:700;color:var(--ink);text-transform:uppercase}
.benefits-title{top:1158px;left:0;width:1200px;text-align:center;font-size:30px}
.benefits-rule{top:1200px;left:580px;width:40px;height:3px;background:var(--olive)}
.card{position:absolute;top:1244px;width:259px}
.card-img{height:208px}
.card h3{margin-top:18px;text-align:center;font-family:"Roboto Condensed",Arial,sans-serif;font-weight:700;font-size:17px;color:var(--ink);text-transform:uppercase}
.card p{margin-top:8px;text-align:center;font-size:10.5px;line-height:16px;color:var(--muted)}
.view-all{top:1601px;left:469px;width:255px;height:47px;background:var(--ink);color:var(--white);font-size:18px}

/* enrollment */
.enroll{top:1697px;left:0;width:1200px;height:170px;background:linear-gradient(90deg,var(--yellow-deep),var(--yellow) 50%,var(--yellow-deep))}
.enroll-title{top:1727px;left:0;width:1200px;text-align:center;font-family:"Roboto Condensed",Arial,sans-serif;font-weight:700;font-size:30px;color:var(--ink)}
.field{position:absolute;display:flex;align-items:center;gap:10px;padding:0 12px;font-size:11px;color:#444}
.field svg{width:13px;height:13px;flex:none}
.enroll-field{top:1796px;height:34px;border:2px solid #5a4a10;background:transparent;color:var(--ink)}
.enroll-btn{top:1796px;left:866px;width:172px;height:34px;background:var(--ink);color:var(--white);font-size:14px}

/* blogs */
.blogs-title{top:1896px;left:161px;font-size:25px}
.blogs-line{top:1932px;left:161px;width:877px;height:1px;background:#999}
.blogs-accent{top:1930px;left:161px;width:95px;height:4px;background:var(--olive)}
.pager{top:1918px;width:13px;height:12px;background:var(--ink);display:flex;align-items:center;justify-content:center}
.pager svg{width:7px;height:7px}
.post{position:absolute;width:422px;height:138px}
.post-img{position:absolute;left:0;top:0;width:183px;height:136px}
.post-date{position:absolute;left:192px;top:0;width:76px;height:64px;background:var(--olive);color:var(--white);text-align:center;font-family:"Roboto Condensed",Arial,sans-serif;font-weight:700;font-size:26px;line-height:28px;padding-top:4px}
.post-title{position:absolute;left:279px;top:0;width:143px;font-weight:700;font-size:12.5px;line-height:17px;color:var(--ink)}
.post-text{position:absolute;left:192px;top:72px;width:230px;font-size:10px;line-height:15px;color:var(--muted)}
.post-stars{position:absolute;left:192px;top:122px;font-size:14px;letter-spacing:1px;color:var(--yellow-deep)}
.post-more{position:absolute;right:0;top:124px;font-size:10px;color:var(--olive)}

/* members */
.members{top:2319px;left:0;width:1200px;height:108px;background:linear-gradient(90deg,#1c1c1c,#2e2e2e 50%,#1c1c1c)}
.members-label{top:2358px;left:161px;font-size:22px;color:#d8d8d8}
.member-field{top:2355px;height:34px;width:243px;border:1px solid #666;color:#aaa}
.members-btn{top:2355px;left:907px;width:131px;height:34px;background:var(--yellow);color:var(--ink);font-size:17px}

/* contact */
.contact{top:2427px;left:0;width:1200px;height:361px;background:linear-gradient(135deg,#d6d6d6,#e4e4e4 50%,#d3d3d3)}
.contact-title{top:2456px;left:161px;font-size:36px}
.contact-rule{top:2500px;left:161px;width:45px;height:3px;background:var(--olive)}
.contact-intro{top:2512px;left:161px;width:560px;font-size:10px;line-height:17px;color:#444}
.cfield{position:absolute;border:1px solid #555;padding:6px 10px;font-size:10.5px;color:#333}
.contact-btn{top:2712px;left:161px;width:124px;height:32px;background:var(--ink);color:var(--white);font-size:13px}
.info-title{top:2572px;left:773px;font-size:20px;font-weight:500;color:var(--ink)}
.info-row{position:absolute;left:773px;display:flex;gap:12px;align-items:flex-start;font-size:10.5px;line-height:14px;color:var(--ink)}
.info-row svg{width:13px;height:13px;flex:none;margin-top:1px}

/* footer */
.footer{top:2788px;left:0;width:1200px;height:47px;background:var(--olive)}
.copyright{top:2806px;left:161px;font-size:10px;color:var(--white)}
.social{top:2805px;left:920px;display:flex;gap:12px}
.social span{width:12px;height:12px;border-radius:50%;background:var(--white)}
</style>
</head>
<body>
<div class="page">

  <div class="abs topbar"></div>
  <div class="abs hero" role="img" aria-label="Photograph of a smiling senior couple sitting close together in a bright home"></div>
  <div class="abs hero-tag">Association<br>for better health</div>
  <div class="abs brand"><span class="brand-name">Unified Household Wellspring Alliance</span></div>

  <div class="abs promo"></div>
  <div class="abs promo-text">The Unified Household Wellspring Alliance free membership</div>
  <div class="btn join">Join now
    <svg viewBox="0 0 16 16"><circle cx="8" cy="8" r="8" fill="currentColor"/><path d="M6.5 4.5 10 8l-3.5 3.5" stroke="#f2c315" stroke-width="2" fill="none"/></svg></div>

  <div class="abs welcome-frame"></div>
  <div class="abs welcome-photo" role="img" aria-label="Photograph of a happy older couple outdoors in autumn, wearing warm scarves"></div>
  <h1 class="abs welcome-title">Welcome to</h1>
  <h2 class="abs welcome-sub">The Unified Household Wellspring Alliance</h2>
  <div class="abs welcome-body">
    <p>Lorem Ipsum is simply dummy text of the printing and typesetting industry. Lorem Ipsum has been the industry's type specimen book. It has survived not only five centuries, but also the leap into electronic typesetting, remaining passages, and more recently with desktop publishing software like Quillset Press including versions of Lorem to make a type specimen book. It has survived not only five centuries, but also the leap into electronic typesetting, Ipsum passages, and more recently with desktop publishing software like Quillset Press including versions of Lorem Ipsum.Lorem Ipsum is simply dummy text of the printing and typesetting industry. Lorem Ipsum has been the Ipsum passages, and more recently with desktop publishing software .</p>
    <p>Lorem Ipsum is simply dummy text of the printing and typesetting industry. Lorem Ipsum has been the industry's type and more recently with desktop publishing software like Quillset Press including versions of Lorem to make a type specimen book. It has survived not only five centuries, but also the leap into electronic typesetting, remaining passages, and more recently with desktop publishing software like Quillset Press including versions of Lorem Ipsum.Lorem Ipsum is simply dummy text of the printing and typesetting industry. Lorem Ipsum has been the Ipsum passages, and more recently with desktop publishing software .</p>
  </div>
  <div class="btn read-more">Read more
    <svg viewBox="0 0 16 16"><circle cx="8" cy="8" r="8" fill="#fff"/><path d="M6.5 4.5 10 8l-3.5 3.5" stroke="#8a9a3e" stroke-width="2" fill="none"/></svg></div>

  <h2 class="abs section-title benefits-title">List of benefits</h2>
  <div class="abs benefits-rule"></div>

  <div class="card" style="left:161px">
    <div class="card-img" role="img" aria-label="Photograph of a team of smiling doctors in white coats" style="background:linear-gradient(180deg,#dfe7ec,#f2f4f5 60%,#cfd8de)"></div>
    <h3>Health services</h3>
    <p>Lorem Ipsum is simply dummy text of the printing and make a type specimen book. It has survived not only five Lorem Ipsum passages, and more recently with desktop publishing software like Quillset</p>
  </div>
  <div class="card" style="left:469px">
    <div class="card-img" role="img" aria-label="Photograph of two young women looking at a tablet outdoors" style="background:linear-gradient(135deg,#5f8a3a,#c24a8e 50%,#2fa79a)"></div>
    <h3>Consumer services</h3>
    <p>Lorem Ipsum is simply dummy text of the printing and make a type specimen book. It has survived not only five Lorem Ipsum passages, and more recently with desktop publishing software like Quillset</p>
  </div>
  <div class="card" style="left:777px">
    <div class="card-img" role="img" aria-label="Photograph of two businessmen shaking hands in front of glass towers" style="background:linear-gradient(135deg,#3f78b8,#a9c9e8 55%,#2b2b2b)"></div>
    <h3>Business services</h3>
    <p>Lorem Ipsum is simply dummy text of the printing and make a type specimen book. It has survived not only five Lorem Ipsum passages, and more recently with desktop publishing software like Quillset</p>
  </div>
  <div class="btn view-all">View all services
    <svg viewBox="0 0 16 16"><circle cx="8" cy="8" r="8" fill="#fff"/><path d="M6.5 4.5 10 8l-3.5 3.5" stroke="#1e1e1e" stroke-width="2" fill="none"/></svg></div>

  <div class="abs enroll"></div>
  <h2 class="abs enroll-title">Membership Enrollment</h2>
  <div class="field enroll-field" style="left:161px;width:340px">
    <svg viewBox="0 0 16 16" fill="#1e1e1e"><circle cx="8" cy="4.5" r="3.5"/><path d="M1.5 16c0-4 3-6.5 6.5-6.5s6.5 2.5 6.5 6.5z"/></svg>Enter your name</div>
  <div class="field enroll-field" style="left:514px;width:338px">
    <svg viewBox="0 0 16 16" fill="none" stroke="#1e1e1e" stroke-width="1.5"><rect x="1" y="3" width="14" height="10"/><path d="m1 3 7 6 7-6"/></svg>Enter your email</div>
  <div class="btn enroll-btn">Enrollment now!</div>

  <h2 class="abs section-title blogs-title">Latest blogs</h2>
  <div class="abs blogs-line"></div>
  <div class="abs blogs-accent"></div>
  <div class="abs pager" style="left:1009px"><svg viewBox="0 0 8 8"><path d="M5.5 1 2.5 4l3 3" stroke="#fff" stroke-width="1.5" fill="none"/></svg></div>
  <div class="abs pager" style="left:1025px"><svg viewBox="0 0 8 8"><path d="M2.5 1l3 3-3 3" stroke="#fff" stroke-width="1.5" fill="none"/></svg></div>

  <article class="post" style="left:161px;top:1958px">
    <div class="post-img" role="img" aria-label="Photograph of a senior man talking with a caregiver" style="background:linear-gradient(135deg,#8aa8c8,#e9e4dc 55%,#b9a48a)"></div>
    <div class="post-date">18<br>DEC</div>
    <h3 class="post-title">Lorem Ipsum simply dummy text of the print-ing and text typesetting industry.</h3>
    <p class="post-text">Lorem Ipsum is simply dummy text of the printing and typesetting industry. Lorem Ipsum has been the leap release Typeleaf sheets containing Lorem</p>
    <div class="post-stars">★★★★★</div><span class="post-more">Read More...</span>
  </article>
  <article class="post" style="left:616px;top:1958px">
    <div class="post-img" role="img" aria-label="Photograph of a smiling couple at a desk in a bright office" style="background:linear-gradient(135deg,#e8e6e2,#cfc7bc 50%,#f4f2ee)"></div>
    <div class="post-date">19<br>DEC</div>
    <h3 class="post-title">Lorem Ipsum simply dummy text of the print-ing and text typesetting industry.</h3>
    <p class="post-text">Lorem Ipsum is simply dummy text of the printing and typesetting industry. Lorem Ipsum has been the leap release Typeleaf sheets containing Lorem</p>
    <div class="post-stars">★★★★★</div><span class="post-more">Read More...</span>
  </article>
  <article class="post" style="left:161px;top:2122px">
    <div class="post-img" role="img" aria-label="Photograph of people exercising on treadmills in a gym" style="background:linear-gradient(135deg,#5a6470,#d9d4cc 55%,#8d8a86)"></div>
    <div class="post-date">20<br>DEC</div>
    <h3 class="post-title">Lorem Ipsum simply dummy text of the print-ing and text typesetting industry.</h3>
    <p class="post-text">Lorem Ipsum is simply dummy text of the printing and typesetting industry. Lorem Ipsum has been the leap release Typeleaf sheets containing Lorem</p>
    <div class="post-stars">★★★★★</div><span class="post-more">Read More...</span>
  </article>
  <article class="post" style="left:616px;top:2122px">
    <div class="post-img" role="img" aria-label="Photograph of a cheerful older couple embracing outdoors" style="background:linear-gradient(135deg,#b6c98a,#e8d9c6 50%,#7aa9c4)"></div>
    <div class="post-date">21<br>DEC</div>
    <h3 class="post-title">Lorem Ipsum simply dummy text of the print-ing and text typesetting industry.</h3>
    <p class="post-text">Lorem Ipsum is simply dummy text of the printing and typesetting industry. Lorem Ipsum has been the leap release Typeleaf sheets containing Lorem</p>
    <div class="post-stars">★★★★★</div><span class="post-more">Read More...</span>
  </article>

  <div class="abs members"></div>
  <div class="abs members-label">Member’s only access</div>
  <div class="field member-field" style="left:391px">Enter your name</div>
  <div class="field member-field" style="left:651px">Enter your name</div>
  <div class="btn members-btn">Submit
    <svg viewBox="0 0 16 16"><circle cx="8" cy="8" r="7" fill="none" stroke="#1e1e1e" stroke-width="1.6"/><path d="M6.5 4.5 10 8l-3.5 3.5" stroke="#1e1e1e" stroke-width="1.8" fill="none"/></svg></div>

  <div class="abs contact" role="img" aria-label="Faint street map background"></div>
  <h2 class="abs section-title contact-title">Contact form</h2>
  <div class="abs contact-rule"></div>
  <p class="abs contact-intro">Lorem Ipsum is simply dummy text of the printing and typesetting industry. Lorem Ipsum has been the industry's standard dummy text Lorem Ipsum is simply dummy text.</p>
  <div class="cfield" style="left:161px;top:2570px;width:274px;height:31px">Name</div>
  <div class="cfield" style="left:446px;top:2570px;width:272px;height:31px">Last Name</div>
  <div class="cfield" style="left:161px;top:2616px;width:274px;height:30px">Email</div>
  <div class="cfield" style="left:446px;top:2616px;width:272px;height:75px">Massage</div>
  <div class="cfield" style="left:161px;top:2661px;width:274px;height:30px">Phone Number</div>
  <div class="btn contact-btn">Submit now
    <svg viewBox="0 0 16 16"><circle cx="8" cy="8" r="7" fill="none" stroke="#fff" stroke-width="1.6"/><path d="M6.5 4.5 10 8l-3.5 3.5" stroke="#fff" stroke-width="1.8" fill="none"/></svg></div>

  <h3 class="abs info-title">Contact Information:-</h3>
  <div class="info-row" style="top:2617px">
    <svg viewBox="0 0 16 16" fill="#1e1e1e"><path d="M8 0a5.5 5.5 0 0 0-5.5 5.5C2.5 10 8 16 8 16s5.5-6 5.5-10.5A5.5 5.5 0 0 0 8 0zm0 8a2.5 2.5 0 1 1 0-5 2.5 2.5 0 0 1 0 5z"/></svg>
    <span>Lorem Ipsum is simply dummy text<br>of the printing and typesetting industry.</span></div>
  <div class="info-row" style="top:2664px;font-size:13px">
    <svg viewBox="0 0 16 16" fill="#1e1e1e"><path d="M3.5 0 6 3.5 4.5 5.5c1 2.5 3.5 5 6 6L12.5 10 16 12.5 14 16C6 15.5.5 10 0 2z"/></svg>
    <span>0400 555 018</span></div>
  <div class="info-row" style="top:2700px">
    <svg viewBox="0 0 16 16" fill="#1e1e1e"><path d="M0 3h16v1.5L8 9 0 4.5zM0 6.2 8 10.7l8-4.5V13H0z"/></svg>
    <span>info@unifiedhouseholdwellspring.org</span></div>

  <div class="abs footer"></div>
  <div class="abs copyright">© 2017 unifiedhouseholdwellspring.org. All rights reserved.</div>
  <div class="abs social" aria-label="Social links"><span></span><span></span><span></span><span></span><span></span></div>

</div>
</body>
</html>
```